Global Nano Technology Surface Protection company needs a new logo and cards

We are a Global company that will apply nanotechnology coatings on surfaces to prevent growth and spread of bacteria, viruses, mold etc. We deal with large corporates, airlines, hospitals and schools so we are after a new modern, simple and clean look that will have great visual impact.
We a company that is focused on prevention and protection.

Company name, Luminary Fabrications Worldwide

Subtext, Antimicrobial Surface Protection

Logo, LFWW or LFW

Target Market(s)

Hospitals, Transport agencies, Airlines, Corporate entities

Industry/Entity Type

Protection

Contact Information for Business Card

Logo, LFWW or LFW
www.lfww.us
Derek Hawtrey
+64213958260
tidyshieldnz@mailbox.example

Logo Text

LFWW

Requirements
Must have
• Simple clean look
Should not have
• Nothing too messy

```html
<!DOCTYPE html>
<html lang="en">
<head>
<meta charset="utf-8">
<title>Luminary Fabrications Worldwide – Business Cards</title>
<link rel="stylesheet" href="https://fonts.googleapis.com/css2?family=Archivo:wght@400;700;800&display=swap">
<style>
  :root {
    --backdrop: #d9dbde;
    --card: #ffffff;
    --green-dark: #0f6b38;
    --green-light: #7cbd3b;
    --card-shadow: 0 10px 28px rgba(0,0,0,0.16);
  }
  * { box-sizing: border-box; margin: 0; padding: 0; }
  html, body { width: 1200px; height: 857px; overflow: hidden; }
  body {
    background: var(--backdrop);
    font-family: "Archivo", Arial, sans-serif;
    display: flex;
    align-items: center;
    justify-content: center;
    gap: 44px;
  }
  .card {
    position: relative;
    width: 520px;
    height: 300px;
    background: var(--card);
    box-shadow: var(--card-shadow);
  }

  /* Back side */
  .card-back .headline {
    position: absolute;
    left: 34px;
    bottom: 92px;
  }
  .company-title {
    color: var(--green-dark);
    font-weight: 800;
    font-size: 19px;
    letter-spacing: 1.2px;
    text-transform: uppercase;
    white-space: nowrap;
  }
  .tagline {
    color: var(--green-light);
    font-size: 13px;
    letter-spacing: 1px;
    margin-top: 3px;
    padding-left: 64px;
  }
  .card-back .brand-mark {
    position: absolute;
    right: 40px;
    top: 64px;
  }
  .brand-mark {
    display: flex;
    align-items: center;
    gap: 8px;
  }
  .brand-mark .dot {
    width: 30px; height: 30px;
    border-radius: 50%;
    background: var(--green-light);
  }
  .brand-mark .initials {
    color: var(--green-dark);
    font-weight: 800;
    font-size: 24px;
    letter-spacing: 1px;
  }

  /* Front side */
  .person-name {
    position: absolute;
    right: 40px;
    top: 44px;
    color: var(--green-dark);
    font-weight: 800;
    font-size: 17px;
    letter-spacing: 1.2px;
  }
  .identity {
    position: absolute;
    left: 34px;
    top: 138px;
    display: flex;
    align-items: center;
    gap: 12px;
  }
  .identity .brand-mark .dot { width: 34px; height: 34px; }
  .identity .divider {
    width: 2px;
    height: 64px;
    background: var(--green-light);
  }
  .stacked-name {
    color: var(--green-dark);
    font-size: 10.5px;
    line-height: 1.15;
    letter-spacing: 0.6px;
    text-transform: uppercase;
  }
  .contact-list {
    position: absolute;
    left: 292px;
    top: 142px;
    list-style: none;
  }
  .contact-list li {
    display: flex;
    align-items: center;
    gap: 7px;
    color: var(--green-light);
    font-size: 12px;
    letter-spacing: 0.5px;
    line-height: 19px;
  }
  .contact-list svg {
    width: 11px; height: 11px;
    flex: none;
    stroke: var(--green-dark);
    fill: none;
    stroke-width: 1.6;
  }
</style>
</head>
<body>

  <section class="card card-back" aria-label="Card back">
    <div class="brand-mark">
      <span class="dot"></span>
      <span class="initials">LFW</span>
    </div>
    <div class="headline">
      <h1 class="company-title">Luminary Fabrications Worldwide</h1>
      <p class="tagline">Antimicobial Surface Proctection</p>
    </div>
  </section>

  <section class="card card-front" aria-label="Card front">
    <p class="person-name">Derek Hawtrey</p>
    <div class="identity">
      <div class="brand-mark">
        <span class="dot"></span>
        <span class="initials">LFW</span>
      </div>
      <span class="divider"></span>
      <p class="stacked-name">Luminary<br>Fabrications<br>Worldwide</p>
    </div>
    <ul class="contact-list">
      <li>
        <svg viewBox="0 0 12 12"><path d="M3 1.5 L5 3.5 L4 5 Q5 7 7 8 L8.5 7 L10.5 9 L9 10.8 Q4 10 1.2 3 Z"/></svg>
        +64 213 958 260
      </li>
      <li>
        <svg viewBox="0 0 12 12"><circle cx="6" cy="6" r="4.8"/><path d="M1.2 6 H10.8 M6 1.2 Q3 6 6 10.8 M6 1.2 Q9 6 6 10.8"/></svg>
        www.lfww.us
      </li>
      <li>
        <svg viewBox="0 0 12 12"><rect x="1" y="2.5" width="10" height="7"/><path d="M1 2.5 L6 6.5 L11 2.5"/></svg>
        tidyshieldnz@mailbox.example
      </li>
    </ul>
  </section>

</body>
</html>
```